New Architectural Firm Business Cards

New Business card to compliment previous pixel harbor logo (attached). Please design a business card that is simple, modern, creative....please do not use "symbols", simply the logo and associated graphics/text. The front should contain name/address/phone/email/web address (with graphics).....back should be 100% graphic design using the logo somehow. Hoping for a two color (black and yellow) design. full bleed design, no borders

Target Market(s)

Commercial Architecture Clients

Industry/Entity Type

Architecture

Contact Information for Business Card

Please design a business card that is simple, modern, creative....please do not use "symbols", simply the logo and associated graphics/text. The front should contain name/address/phone/email/web address (with graphics).....back should be 100% graphic design using the logo somehow

Font styles to use
Sans Serif

Colors
FFF300
FFF600
FEFA6F
FFFEC7
FFFEE8

Requirements
Must have
• Clean, Modern Design
Should not have
• Stock images or "icons"

```html
<!DOCTYPE html>
<html lang="en">
<head>
<meta charset="utf-8">
<title>Pixel Harbor – Business Cards</title>
<link rel="stylesheet" href="https://fonts.googleapis.com/css2?family=Poppins:wght@300;400;600;700&display=swap">
<style>
  :root {
    --brand-yellow: #ebb81c;
    --backdrop: #e9c64a;
    --card-white: #fbfbfa;
    --ink: #1f1f1f;
    --ink-soft: #3a3a3a;
  }
  * { margin: 0; padding: 0; box-sizing: border-box; }
  html, body {
    width: 1200px;
    height: 800px;
    overflow: hidden;
  }
  body {
    background: var(--backdrop);
    font-family: "Poppins", sans-serif;
    color: var(--ink);
    display: flex;
    align-items: center;
    justify-content: center;
    gap: 60px;
  }
  .card {
    width: 520px;
    height: 297px;
    background: var(--card-white);
    position: relative;
  }

  /* Brand side */
  .card--brand {
    display: flex;
    flex-direction: column;
    align-items: center;
    justify-content: center;
  }
  .brand-name {
    display: flex;
    align-items: center;
    gap: 14px;
    margin-top: -30px;
  }
  .brand-name__dot {
    width: 22px;
    height: 22px;
    border-radius: 50%;
    background: var(--brand-yellow);
  }
  .brand-name__text {
    font-weight: 700;
    font-size: 44px;
    letter-spacing: -0.5px;
    color: var(--brand-yellow);
  }
  .contact-strip {
    position: absolute;
    left: 0;
    right: 0;
    bottom: 26px;
    text-align: center;
    font-size: 12.5px;
    font-weight: 400;
    color: var(--ink);
  }
  .contact-strip .sep {
    color: var(--brand-yellow);
    margin: 0 8px;
  }

  /* Details side */
  .card--details {
    padding: 38px 40px 0;
    text-align: center;
  }
  .holder-name {
    font-weight: 700;
    font-size: 25px;
    letter-spacing: 0.2px;
    line-height: 1.1;
  }
  .holder-role {
    font-weight: 400;
    font-size: 16px;
    color: var(--brand-yellow);
    margin-bottom: 14px;
  }
  .direct-lines {
    font-weight: 300;
    font-size: 16px;
    line-height: 1.4;
    color: var(--ink-soft);
  }
  .offices {
    margin-top: 22px;
    font-size: 11.5px;
    font-weight: 400;
    line-height: 1.55;
    color: var(--ink-soft);
  }
  .offices strong { font-weight: 600; color: var(--ink); }
  .offices sup { font-size: 7px; }
  .corner-name {
    position: absolute;
    left: 24px;
    bottom: 18px;
    font-weight: 700;
    font-size: 14px;
    color: var(--brand-yellow);
  }
</style>
</head>
<body>
  <section class="card card--brand" aria-label="Card brand side">
    <div class="brand-name">
      <span class="brand-name__dot"></span>
      <span class="brand-name__text">Pixel Harbor</span>
    </div>
    <p class="contact-strip">
      +01 555 00 12 12<span class="sep">|</span>info@pixelharbor.com<span class="sep">|</span>www.pixelharbor.com
    </p>
  </section>

  <section class="card card--details" aria-label="Card details side">
    <h1 class="holder-name">CARD HOLDER</h1>
    <p class="holder-role">Designation here</p>
    <p class="direct-lines">
      + 01 555 344 210 (USA)<br>
      + 01 555 730 418 (TZ)<br>
      mara@pixelharbor.com
    </p>
    <p class="offices">
      <strong>Headquarters:</strong> P.O Box 90, Harbor City<br>
      <strong>Liaison Office:</strong> 2<sup>nd</sup> Floor, Quay Towers<br>
      Marlow Rd, Eastport
    </p>
    <span class="corner-name">Pixel Harbor</span>
  </section>
</body>
</html>
```